Q7L Holdings Inc.
Thank you designers for all your great work.
Correction, please change #64 & #61. not #63
Hi BirchVelo, on #63 & #64, could you organize the information (phone, address, etc.) like loaded example BizCardExample2. "DRE #" right below agent name.
Can you change the sentence to be more grammatically correct:
1: Making a difference from home to home
2: It begins here: www.q7lhx.example
Thank you.
Hi Birchvelo, I love #58. can you have color theme green for "Funding" and orange for "Real Estate". Please update the word accordingly to color theme.
In the back of Biz card I would like to add the follow lines:
1: "Make a difference from home to home"
(at any place that look good)
2: "It begin here: www.Q7LHX.example"
(at the bottom right)
Hi BirchVelo, could you have number 2 same as back side to see how it look regardless that it hit the logo.
Hi Birchvelo, for #38 an #40, I'm not sure my previous suggest make it look better. number 2 going to hit the logo if you make it same as back side. Could move/size it around to see how it look. thanks.
Hi Birchvelo, on #38 & #40 could you change the front biz card rotate number 2 to be same as the back of biz. keep the color the same. Could you design stationary for me also.
Hi Lumbar, on #18, could you change the background green/blue to black, and the big number 2 to green or orange. and other change as you feel fit.
a suggestion, try to have the 2 in q7l as green/orange and have h in white and have background in dark color.
Birchvelo, I like #21 back of biz card. Can you play around with the background (like black/grey) to make the logo more stand out. Please change the logo color to brighter blue/green/orange color if necessary.
Corvix, #19 can you change the gray background to black and make sure the logo and word to be bright. You can change the orange/blue/green into a bright orange/blue/green.
Hi, I have upload some Biz card example that I found on the web. I hope this help designer to get an idea on what I'm looking for.
lumbar, I prefer to keep the logo color same as there are.
Hi Lumbar, I like #18 design, it going to the right direction on what I'm looking for. Could you play around with the color to make it brighter.
pelltorvan, thank you for submitting with the gray background. I didnt think it look that dark. I have an example business card that have gray back ground but it look bright. Hm...
Please have design that make it look bright.
plz upload the ai or eps file
I like a dark gray background to have the logo stand out.
the cluster is an example. You can cluster info that you think is better.
I guess we can cluster info together:
1) 1200 Maple Ave, Suite 4, Riverton, CA 90000, website, and (555) 014-2280 is together.
2) cell phone, fax, email and DRE# is together.
3) take out toll free number.
Sorry for the wrong briefing. Q7L RE color theme blue/orange. Q7L Funding color theme is blue/green. On the back of the business is like a promotional flyer where promotional is stand out trying to attract customer to notice.
pelltorvan, the design need to have room for agent image on the front of the business card.
#1 to #7: The design is too simple and blank, need more creativity. Information look too cluster where it can be confusing. Could we have a design in a way that when the information is given doesn't look messy.
2) cell phone, fax and DRE# is together.

```html
<!DOCTYPE html>
<html lang="en">
<head>
<meta charset="utf-8">
<title>Q7L Holdings Inc. — Stationery Set</title>
<link href="https://fonts.googleapis.com/css2?family=Oswald:wght@500&family=Open+Sans:wght@400;600&display=swap" rel="stylesheet">
<style>
  :root{
    --board:#3b3b3b;
    --paper:#ffffff;
    --ink-black:#0d0d0d;
    --brand-green:#4cb848;
    --brand-blue:#2a5aa8;
    --faint-green:#dcefd9;
    --label:#d8d8d8;
    --small-text:#555b62;
    --mark:#9a9a9a;
  }
  html,body{margin:0;padding:0;overflow:hidden;background:var(--board);}
  .board{display:block;width:1200px;height:874px;}
  .section-label{font-family:"Open Sans",sans-serif;font-size:10px;font-weight:600;fill:var(--label);letter-spacing:.6px;}
  .brand-name{font-family:"Oswald",sans-serif;font-weight:500;fill:var(--brand-blue);letter-spacing:.5px;}
  .brand-name.on-dark{fill:var(--paper);}
  .brand-dot{fill:var(--brand-green);}
  .contact{font-family:"Open Sans",sans-serif;font-size:5.5px;fill:var(--small-text);}
  .contact.on-dark{fill:#cfcfcf;}
  .promo{font-family:"Open Sans",sans-serif;font-size:9px;fill:var(--paper);letter-spacing:.3px;}
  .crop{stroke:var(--mark);stroke-width:.8;fill:none;}
  .paper{fill:var(--paper);}
  .dark{fill:var(--ink-black);}
  .band{fill:var(--brand-green);}
</style>
</head>
<body>
<svg class="board" viewBox="0 0 1200 874" xmlns="http://www.w3.org/2000/svg">
  <defs>
    <radialGradient id="faintGreen" cx="50%" cy="50%" r="50%">
      <stop offset="0" stop-color="#cfe9cb" stop-opacity=".9"/>
      <stop offset="1" stop-color="#cfe9cb" stop-opacity="0"/>
    </radialGradient>
    <radialGradient id="faintGrey" cx="50%" cy="50%" r="50%">
      <stop offset="0" stop-color="#555" stop-opacity=".8"/>
      <stop offset="1" stop-color="#555" stop-opacity="0"/>
    </radialGradient>
  </defs>

  <!-- Pocket folder outside -->
  <text class="section-label" x="28" y="26">POCKET FOLDER | OUTSIDE</text>
  <g class="folder-outside">
    <rect class="paper" x="34" y="43" width="278" height="384"/>
    <rect class="dark" x="312" y="43" width="317" height="384"/>
    <ellipse role="img" aria-label="Faint large brand numeral decoration" cx="150" cy="300" rx="110" ry="70" fill="url(#faintGreen)"/>
    <ellipse role="img" aria-label="Grey large brand numeral decoration" cx="470" cy="230" rx="140" ry="130" fill="url(#faintGrey)"/>
    <rect class="band" x="34" y="420" width="595" height="7"/>

    <rect class="brand-dot" x="50" y="300" width="14" height="14"/>
    <text class="brand-name" x="70" y="313" font-size="15">Q7L HOLDINGS</text>
    <text class="contact" x="50" y="382">Email: info@q7lhx.example | Web: www.Q7LHX.example | DRE No: 01234567</text>
    <text class="contact" x="50" y="392">Ph: (555) 014-2280 | Fax: (555) 014-2281 | Cell: (555) 014-2282</text>
    <text class="contact" x="50" y="402">1200 Maple Ave, Suite 4, Riverton, CA 90000</text>

    <rect class="brand-dot" x="336" y="62" width="14" height="14"/>
    <text class="brand-name on-dark" x="356" y="75" font-size="15">Q7L HOLDINGS</text>
    <text class="promo" x="440" y="364">Promotion • Promotion • Promotion</text>
    <text class="promo" x="440" y="380">Service • Service • Service • Service</text>

    <path class="crop" d="M22 120v40M22 300v40M640 120v40M640 300v40"/>
  </g>

  <!-- Letter head -->
  <text class="section-label" x="653" y="26">LETTER HEAD</text>
  <g class="letterhead">
    <rect class="paper" x="653" y="48" width="199" height="264"/>
    <ellipse role="img" aria-label="Faint large brand numeral decoration" cx="750" cy="170" rx="80" ry="90" fill="url(#faintGreen)"/>
    <rect class="brand-dot" x="664" y="58" width="9" height="9"/>
    <text class="brand-name" x="677" y="67" font-size="10">Q7L HOLDINGS</text>
    <text class="contact" x="662" y="296" font-size="4">1200 Maple Ave, Riverton CA | (555) 014-2280</text>
    <rect class="band" x="653" y="301" width="199" height="11"/>
  </g>

  <!-- Envelope -->
  <text class="section-label" x="880" y="26">ENVELOPE</text>
  <g class="envelope">
    <rect class="paper" x="869" y="53" width="295" height="163"/>
    <path class="band" d="M869 53H1164L1016 96Z"/>
    <ellipse role="img" aria-label="Faint large brand numeral decoration" cx="1040" cy="150" rx="90" ry="60" fill="url(#faintGreen)"/>
    <rect class="brand-dot" x="880" y="104" width="9" height="9"/>
    <text class="brand-name" x="893" y="113" font-size="10">Q7L HOLDINGS</text>
    <text class="contact" x="1060" y="120" font-size="4.5">Recipient Name</text>
    <text class="contact" x="1060" y="128" font-size="4.5">Street Address Line</text>
    <text class="contact" x="1060" y="136" font-size="4.5">City, State 00000</text>
  </g>

  <!-- Business cards -->
  <g class="business-cards">
    <rect class="paper" x="955" y="252" width="101" height="53"/>
    <rect class="brand-dot" x="961" y="259" width="6" height="6"/>
    <text class="brand-name" x="970" y="265" font-size="7">Q7L HOLDINGS</text>
    <text class="contact" x="961" y="285" font-size="3.5">Agent Name | DRE 01234567</text>
    <text class="contact" x="961" y="291" font-size="3.5">(555) 014-2282 | info@q7lhx.example</text>
    <rect class="band" x="955" y="301" width="101" height="4"/>

    <rect class="dark" x="955" y="338" width="101" height="53"/>
    <rect class="brand-dot" x="961" y="345" width="6" height="6"/>
    <text class="brand-name on-dark" x="970" y="351" font-size="7">Q7L HOLDINGS</text>
    <text class="contact on-dark" x="990" y="384" font-size="3.5">It begins here: www.Q7LHX.example</text>
    <text class="section-label" x="955" y="407" font-size="8">BUSINESS CARD</text>
  </g>

  <!-- Pocket folder inside -->
  <text class="section-label" x="28" y="452">POCKET FOLDER | INSIDE</text>
  <g class="folder-inside">
    <rect class="paper" x="29" y="468" width="780" height="384"/>
    <ellipse role="img" aria-label="Faint large brand numeral decoration" cx="330" cy="600" rx="230" ry="110" fill="url(#faintGreen)"/>
    <path class="band" d="M29 749H290L310 790L330 749H809V852H29Z"/>
    <path d="M300 852L310 800L320 852Z" fill="var(--board)"/>
    <rect class="brand-dot" x="42" y="482" width="9" height="9"/>
    <text class="brand-name" x="55" y="491" font-size="10">Q7L HOLDINGS</text>
    <rect class="brand-dot" x="556" y="476" width="12" height="12"/>
    <text class="brand-name" x="0" y="0" font-size="16" fill-opacity=".7" transform="translate(566 500) rotate(90)">Q7L HOLDINGS</text>
    <text class="brand-name on-dark" x="228" y="782" font-size="7">Q7L HOLDINGS</text>
    <text class="brand-name on-dark" x="348" y="782" font-size="7">Q7L HOLDINGS</text>
  </g>
</svg>
</body>
</html>
```